Design 5 colour schemes for one web page

We are looking for 5 different colour schemes for our product template to create different kinds of colour tone for our web page, it doesn't need to be restructure the layout, just need to provide different color solution.

Please refer to the attached images and take note of the following when you’re working on the design:
(1) Please precisely reproduce the layout. Cannot remove or delete any wordings, components or column shown in the images.
(2) Okay to revise icons, background color or text style as you prefer. But cannot move/delete them.
(3) Provide PSD source files with good layer management. HTML/CSS are not required.
(4) Make reasonable and professional design.

After completion, please send back:
(1) 5 images with 5 different colour schemes.
(2) Related PSD files.

Font styles to use
Serif
Sans Serif

Requirements
Must have
• (1) 5 images for the colour schemes.
• (2) 5 PSD source files with good layer management.
Nice to have
• (1) Explanation about your design of the colour schemes.
Should not have
• (1) HTML/CSS code are not required.

```html
<!DOCTYPE html>
<html lang="en">
<head>
<meta charset="utf-8">
<title>Sports Betting – Today</title>
<link href="https://fonts.googleapis.com/css2?family=Nunito+Sans:wght@300;400;600&display=swap" rel="stylesheet">
<style>
:root{
  --accent:#2f6fd6;
  --accent-dark:#2258b3;
  --accent-light:#dde8fa;
  --dark:#1f2a3a;
  --darker:#162030;
  --bar:#2e3d54;
  --page:#d3d8e0;
  --side-row:#eef1f5;
  --muted-head:#dfe4ec;
  --line:#cfd5de;
  --text:#222a36;
  --white:#ffffff;
  --badge:#f08a24;
}
*{box-sizing:border-box;margin:0;padding:0}
html,body{width:902px;height:1200px;overflow:hidden}
body{background:var(--page);font-family:"Nunito Sans",Arial,sans-serif;color:var(--text);position:relative}
.abs{position:absolute}
svg.ic{display:inline-block;vertical-align:middle}

/* top bar */
.topbar{left:0;top:0;width:902px;height:35px;background:var(--dark);color:var(--white);font-size:9.5px}
.topnav{left:83px;top:12px;display:flex;gap:8px;align-items:center}
.topnav .sep{opacity:.7}
.badge{background:var(--badge);border-radius:2px;padding:0 3px;font-size:8px}
.greet{left:526px;top:12px}
.balance{left:598px;top:6px;width:128px;height:24px;border:1px solid var(--accent);display:flex;align-items:center;justify-content:center;gap:5px}
.signout{left:739px;top:6px;width:78px;height:24px;border:1px solid var(--accent);display:flex;align-items:center;justify-content:center;font-size:10px}

/* header */
.header{left:83px;top:35px;width:736px;height:55px;background:var(--accent)}
.logo{left:0;top:0;width:115px;height:55px;background:var(--accent-dark);color:var(--white);font-size:35px;font-weight:300;display:flex;align-items:center;padding-left:14px}
.tab-sports{left:379px;top:0;width:67px;height:55px;background:var(--dark);color:var(--white);font-size:13px;text-align:center;padding-top:18px}
.tab-sports::after{content:"";position:absolute;left:28px;bottom:0;border:6px solid transparent;border-bottom-color:var(--white)}
.results{right:15px;top:20px;font-size:10px;color:var(--white);display:flex;gap:8px;align-items:center}

.toolbar{left:83px;top:90px;width:736px;height:31px;background:var(--white);font-size:11px}
.toolbar .item{position:absolute;top:9px;display:flex;align-items:center;gap:6px}
.toolbar .vsep{position:absolute;top:8px;width:1px;height:16px;background:var(--line)}

/* sidebar */
.fav-title{left:99px;top:129px;font-size:12px;color:#4a5566}
.fav-box{left:84px;top:149px;width:122px;height:33px;border:1px solid var(--accent);font-size:8px;text-align:center;line-height:11px;padding-top:5px;color:#3c4656}
.sidebar{left:83px;top:196px;width:143px;height:1004px;background:var(--dark)}
.side-tabs{display:flex;height:31px}
.side-tabs div{flex:1;display:flex;align-items:center;justify-content:center;font-size:11.5px}
.side-tabs .on{background:var(--accent);color:var(--white)}
.side-tabs .off{background:#cdd3dc;color:#3c4656}
.sport{display:flex;height:31.6px;border-bottom:1px solid var(--line);background:var(--side-row)}
.sport .ico{width:37px;background:var(--accent);display:flex;align-items:center;justify-content:center}
.sport .name{flex:1;font-size:9px;padding-left:8px;display:flex;align-items:center;white-space:nowrap}
.sport .count{width:30px;font-size:9px;display:flex;align-items:center}
.ticket-tabs{display:flex;height:34px}
.ticket-tabs div{display:flex;align-items:center;justify-content:center;font-size:11.5px;color:var(--white)}
.ticket-tabs .on{width:68px;background:var(--accent)}
.ticket-tabs .off{flex:1;background:var(--darker)}
.mybets{text-align:center;color:var(--white);font-size:11.5px;margin-top:14px}
.refresh{text-align:center;color:var(--white);font-size:9.5px;margin-top:17px;display:flex;justify-content:center;gap:6px;align-items:center}
.pending{margin:14px 0 0 9px;width:126px;height:30px;border:1px solid var(--accent);color:var(--white);font-size:9px;display:flex;align-items:center;justify-content:center}
.viewall{margin-top:20px;height:25px;background:var(--accent);color:var(--white);font-size:11.5px;display:flex;align-items:center;justify-content:center}
.copy{color:var(--white);font-size:9px;text-align:center;line-height:15px;margin-top:24px}

/* market tables */
.market{left:242px;width:577px;background:var(--white)}
.market-head{height:27px;display:flex;align-items:center;padding:0 14px;font-size:11px}
.live .market-head{background:var(--accent);color:var(--white)}
.nonlive .market-head{background:var(--muted-head);color:var(--text)}
.market-head .title{display:flex;gap:8px;align-items:center;width:260px}
.market-head .count{display:flex;gap:8px;align-items:center;flex:1}
.market-head .league-sel{display:flex;gap:6px;align-items:center}
.grid{display:grid;grid-template-columns:71px 125px 44px 44px 42px 46px 44px 38px 49px 74px}
.cols{height:43px;font-size:10.5px;position:relative}
.live .cols{background:var(--accent-light)}
.cols .c{display:flex;align-items:center;justify-content:center;border-left:1px solid #b7c0cd}
.cols .span2{grid-row:1 / span 2}
.cols .ft{grid-column:3 / span 4;border-bottom:1px solid #b7c0cd}
.cols .fh{grid-column:7 / span 3;border-bottom:1px solid #b7c0cd}
.cols .c.first{border-left:none}
.cols .c.more{font-size:9.5px}
.league{height:23.6px;background:var(--bar);color:var(--white);font-size:10.5px;display:flex;align-items:center;padding:0 12px;gap:8px}
.league .name{flex:1}
.row{height:52.5px;border-bottom:1px solid var(--line);font-size:9.5px}
.live .row{height:47px;background:var(--accent-light);border-bottom:none}
.row > div{display:flex;align-items:center;justify-content:center;text-align:center;line-height:13px;white-space:nowrap}
.row .time{justify-content:flex-start;gap:10px;padding-left:9px;border-right:1px solid var(--line)}
.row .ev{justify-content:flex-start;text-align:left;gap:5px;padding-left:5px;border-right:1px solid var(--line)}
.row .x12{border-right:1px solid var(--line)}
.row .more{font-size:10.5px;gap:3px;grid-column:10;font-weight:600}

.footer{left:242px;top:1169px;width:577px;text-align:center;font-size:9px;color:#3c4656}
.footer span{margin:0 5px}
</style>
</head>
<body>
<svg width="0" height="0" style="position:absolute">
  <symbol id="i-refresh" viewBox="0 0 16 16"><path d="M13 6a5.5 5.5 0 0 0-10-1M3 10a5.5 5.5 0 0 0 10 1" fill="none" stroke="currentColor" stroke-width="2"/><path d="M13.5 1.5v5h-5z M2.5 14.5v-5h5z" fill="currentColor"/></symbol>
  <symbol id="i-star" viewBox="0 0 16 16"><path d="M8 1l2.1 4.6 5 .5-3.8 3.3 1.1 5L8 11.8 3.6 14.4l1.1-5L.9 6.1l5-.5z" fill="currentColor"/></symbol>
  <symbol id="i-chart" viewBox="0 0 14 12"><path d="M1 11h12" stroke="currentColor"/><rect x="2" y="6" width="2" height="5" fill="currentColor"/><rect x="5" y="3" width="2" height="8" fill="currentColor"/><rect x="8" y="5" width="2" height="6" fill="currentColor"/><path d="M2 5l4-3 3 2 4-3" fill="none" stroke="currentColor"/></symbol>
  <symbol id="i-updown" viewBox="0 0 8 12"><path d="M4 0l4 5H0z M4 12l4-5H0z" fill="currentColor"/></symbol>
  <symbol id="i-dot" viewBox="0 0 14 14"><circle cx="7" cy="7" r="5" fill="none" stroke="currentColor" stroke-width="1.6"/><circle cx="7" cy="7" r="1.8" fill="currentColor"/></symbol>
  <symbol id="i-cup" viewBox="0 0 12 14"><path d="M2 0h8v4a4 4 0 0 1-8 0z M5 8h2v3H5z M3 11h6v3H3z" fill="currentColor"/></symbol>
  <symbol id="i-caret" viewBox="0 0 8 5"><path d="M0 0h8L4 5z" fill="currentColor"/></symbol>
  <symbol id="i-runner" viewBox="0 0 12 16"><circle cx="7" cy="2" r="1.8" fill="currentColor"/><path d="M6 5l-3 4 3 1-1 5 M6 5l2 4 3-1 M3 6l3-1" fill="none" stroke="currentColor" stroke-width="1.6"/></symbol>
</svg>

<div class="abs topbar">
  <div class="abs topnav">My Bets <span class="sep">|</span> Statement <span class="sep">|</span> Preferences <span class="sep">|</span> Announcments <span class="badge">99+</span></div>
  <div class="abs greet">Hi, Stwtg036</div>
  <div class="abs balance">&gt;&gt;&nbsp; SD$ &nbsp;10,072.00 <svg class="ic" width="13" height="13" style="color:#fff"><use href="#i-refresh"/></svg></div>
  <div class="abs signout">Sign Out</div>
</div>

<div class="abs header">
  <div class="abs logo">Logo</div>
  <div class="abs tab-sports">Sports</div>
  <div class="abs results"><svg class="ic" width="9" height="11"><rect x="1" y="1" width="7" height="9" fill="none" stroke="#fff"/><rect x="3" y="5" width="3" height="4" fill="#fff"/></svg>Results</div>
</div>

<div class="abs toolbar">
  <div class="item" style="left:15px"><svg class="ic" width="15" height="15" viewBox="0 0 16 16"><circle cx="8" cy="8" r="7" fill="none" stroke="#222a36" stroke-width="1.4"/><path d="M1 8h14M8 1v14M3 4h10M3 12h10" stroke="#222a36"/></svg>English (Asia)</div>
  <div class="vsep" style="left:131px"></div>
  <div class="item" style="left:162px"><svg class="ic" width="16" height="15" viewBox="0 0 16 15"><rect x="1" y="2" width="14" height="12" fill="none" stroke="#222a36" stroke-width="1.4"/><path d="M1 5h14M4 0v4M12 0v4M4 8h2M7 8h2M10 8h2M4 11h2M7 11h2M10 11h2" stroke="#222a36"/></svg>&nbsp;Nov, 19, 2014 11 : 40 AM</div>
  <div class="item" style="left:511px"><svg class="ic" width="16" height="14" viewBox="0 0 16 14"><rect x="1" y="1" width="11" height="11" fill="none" stroke="#222a36"/><path d="M3 4h7M3 7h5" stroke="#222a36"/><circle cx="12" cy="10" r="3.5" fill="#fff" stroke="#222a36"/></svg><svg class="ic" width="7" height="5"><use href="#i-caret"/></svg></div>
  <div class="vsep" style="left:545px"></div>
  <div class="item" style="left:551px"><svg class="ic" width="14" height="14" style="color:#222a36"><use href="#i-star"/></svg><svg class="ic" width="7" height="5"><use href="#i-caret"/></svg></div>
  <div class="vsep" style="left:578px"></div>
  <div class="item" style="left:585px">My <svg class="ic" width="7" height="5"><use href="#i-caret"/></svg></div>
  <div class="vsep" style="left:617px"></div>
  <div class="item" style="left:627px"><svg class="ic" width="15" height="13" viewBox="0 0 15 13"><path d="M1 4h3l4-3v11L4 9H1z" fill="#222a36"/><path d="M10 4q2 2.5 0 5M12 2q4 4.5 0 9" fill="none" stroke="#222a36"/></svg></div>
  <div class="vsep" style="left:654px"></div>
  <div class="item" style="left:664px;top:6px"><svg class="ic" width="17" height="16" viewBox="0 0 17 16"><rect x="1" y="4" width="15" height="11" fill="none" stroke="#222a36" stroke-width="1.4"/><path d="M5 0l3.5 4L12 0" fill="none" stroke="#222a36"/></svg></div>
  <div class="vsep" style="left:692px"></div>
  <div class="item" style="left:702px">Live</div>
</div>

<div class="abs fav-title">MY FAVOURITES</div>
<div class="abs fav-box">Click An Event Or League<br>To Add It To “My Favourites”</div>

<div class="abs sidebar">
  <div class="side-tabs"><div class="on">SPORTS</div><div class="off">MARKETS</div></div>
  <div class="sport"><div class="ico"><svg width="13" height="13" style="color:#fff"><use href="#i-dot"/></svg></div><div class="name">Football</div><div class="count">600</div></div>
  <div class="sport"><div class="ico"><svg width="13" height="13" style="color:#fff"><use href="#i-dot"/></svg></div><div class="name">Basketball</div><div class="count">600</div></div>
  <div class="sport"><div class="ico"><svg width="13" height="13" style="color:#fff"><use href="#i-dot"/></svg></div><div class="name">Baseball</div><div class="count">600</div></div>
  <div class="sport"><div class="ico"><svg width="13" height="13" style="color:#fff"><use href="#i-dot"/></svg></div><div class="name">Tennis</div><div class="count">600</div></div>
  <div class="sport"><div class="ico"><svg width="13" height="13" style="color:#fff"><use href="#i-dot"/></svg></div><div class="name">US Football</div><div class="count">600</div></div>
  <div class="sport"><div class="ico"><svg width="13" height="13" style="color:#fff"><use href="#i-dot"/></svg></div><div class="name">Badminton</div><div class="count">600</div></div>
  <div class="sport"><div class="ico"><svg width="13" height="13" style="color:#fff"><use href="#i-dot"/></svg></div><div class="name">Boxing</div><div class="count">600</div></div>
  <div class="sport"><div class="ico"><svg width="13" height="13" style="color:#fff"><use href="#i-dot"/></svg></div><div class="name">Cricket</div><div class="count">600</div></div>
  <div class="sport"><div class="ico"><svg width="13" height="13" style="color:#fff"><use href="#i-dot"/></svg></div><div class="name">Cycling</div><div class="count">600</div></div>
  <div class="sport"><div class="ico"><svg width="13" height="13" style="color:#fff"><use href="#i-dot"/></svg></div><div class="name">Darts</div><div class="count">600</div></div>
  <div class="sport"><div class="ico"><svg width="13" height="13" style="color:#fff"><use href="#i-dot"/></svg></div><div class="name">Entertainment</div><div class="count">600</div></div>
  <div class="sport"><div class="ico"><svg width="13" height="13" style="color:#fff"><use href="#i-dot"/></svg></div><div class="name">Golf</div><div class="count">600</div></div>
  <div class="sport"><div class="ico"><svg width="13" height="13" style="color:#fff"><use href="#i-dot"/></svg></div><div class="name">Handball</div><div class="count">600</div></div>
  <div class="sport"><div class="ico"><svg width="13" height="13" style="color:#fff"><use href="#i-dot"/></svg></div><div class="name">Ice Hockey</div><div class="count">600</div></div>
  <div class="sport"><div class="ico"><svg width="13" height="13" style="color:#fff"><use href="#i-dot"/></svg></div><div class="name">Martial Arts</div><div class="count">600</div></div>
  <div class="sport"><div class="ico"><svg width="13" height="13" style="color:#fff"><use href="#i-dot"/></svg></div><div class="name">Motor Sports</div><div class="count">600</div></div>
  <div class="sport"><div class="ico"><svg width="13" height="13" style="color:#fff"><use href="#i-dot"/></svg></div><div class="name">Snooker</div><div class="count">600</div></div>
  <div class="sport"><div class="ico"><svg width="13" height="13" style="color:#fff"><use href="#i-dot"/></svg></div><div class="name">Rugby</div><div class="count">600</div></div>
  <div class="sport"><div class="ico"><svg width="13" height="13" style="color:#fff"><use href="#i-dot"/></svg></div><div class="name">Voleyball</div><div class="count">600</div></div>
  <div class="sport"><div class="ico"><svg width="13" height="13" style="color:#fff"><use href="#i-dot"/></svg></div><div class="name">Winter Sports</div><div class="count">600</div></div>
  <div class="ticket-tabs"><div class="on">TICKET</div><div class="off">PARLAYS 0</div></div>
  <div class="mybets">MY BETS</div>
  <div class="refresh"><svg class="ic" width="14" height="14" style="color:#fff"><use href="#i-refresh"/></svg>REFRESH</div>
  <div class="pending">No Pending Bets</div>
  <div class="viewall">VIEW ALL</div>
  <div class="copy">© 2014 - Betting<br>All Rights Reserved.</div>
</div>

<section class="abs market live" style="top:138px">
  <div class="market-head">
    <div class="title"><svg class="ic" width="11" height="14" style="color:#fff"><use href="#i-runner"/></svg>TODAY LIVE</div>
    <div class="count"><svg class="ic" width="14" height="14" style="color:#fff"><use href="#i-refresh"/></svg>38</div>
    <div class="league-sel"><svg class="ic" width="10" height="12" style="color:#fff"><use href="#i-cup"/></svg>Select League <svg class="ic" width="8" height="5" style="color:#fff"><use href="#i-caret"/></svg></div>
  </div>
  <div class="grid cols">
    <div class="c span2 first">Time</div><div class="c span2">Events</div>
    <div class="c ft">Full Time</div><div class="c fh">First Half</div>
    <div class="c span2 more" style="grid-column:10;grid-row:1 / span 2">+More</div>
    <div class="c">A 1×2</div><div class="c">HDP</div><div class="c">OU</div><div class="c">1×2</div><div class="c">HDP</div><div class="c">OU</div><div class="c">1×2</div>
  </div>
  <div class="league"><svg class="ic" width="11" height="11" style="color:#fff"><use href="#i-star"/></svg><span class="name">Southern Coast Premier league</span><svg class="ic" width="14" height="14" style="color:#fff"><use href="#i-refresh"/></svg></div>
  <div class="grid row">
    <div class="time"><svg width="13" height="11" style="color:var(--accent)"><use href="#i-chart"/></svg><span>16 : 30<br>Live</span></div>
    <div class="ev"><svg width="10" height="10" style="color:#222a36"><use href="#i-star"/></svg><span>Harbour Mariners<br>Riverside Victory</span></div>
    <div>0-0.5</div><div>0.77<br>-0.95</div><div>6-6.5</div><div class="x12">O -0.85<br>U -0.65</div>
    <div class="more"><svg width="7" height="10" style="color:var(--accent)"><use href="#i-updown"/></svg>13</div>
  </div>
</section>

<section class="abs market nonlive" style="top:296px">
  <div class="market-head">
    <div class="title"><svg class="ic" width="11" height="14" style="color:#222a36"><use href="#i-runner"/></svg>TODAY NON LIVE</div>
    <div class="count"><svg class="ic" width="14" height="14" style="color:#222a36"><use href="#i-refresh"/></svg>38</div>
    <div class="league-sel"><svg class="ic" width="10" height="12" style="color:#222a36"><use href="#i-cup"/></svg>Select League <svg class="ic" width="8" height="5" style="color:#222a36"><use href="#i-caret"/></svg></div>
  </div>
  <div class="grid cols">
    <div class="c span2 first">Time</div><div class="c span2">Events</div>
    <div class="c ft">Full Time</div><div class="c fh">First Half</div>
    <div class="c span2 more" style="grid-column:10;grid-row:1 / span 2">+More</div>
    <div class="c">A 1×2</div><div class="c">HDP</div><div class="c">OU</div><div class="c">1×2</div><div class="c">HDP</div><div class="c">OU</div><div class="c">1×2</div>
  </div>

  <div class="league"><svg class="ic" width="11" height="11" style="color:#fff"><use href="#i-star"/></svg><span class="name">Southern Coast Premier league</span><svg class="ic" width="14" height="14" style="color:#fff"><use href="#i-refresh"/></svg></div>
  <div class="grid row"><div class="time"><svg width="13" height="11" style="color:var(--accent)"><use href="#i-chart"/></svg><span>16 : 30<br>Live</span></div><div class="ev"><svg width="10" height="10" style="color:#222a36"><use href="#i-star"/></svg><span>Harbour Mariners<br>Riverside Victory<br>Draw</span></div><div>0-0.5</div><div>0.77<br>-0.95</div><div>6-6.5</div><div class="x12">O -0.85<br>U -0.65</div><div class="more"><svg width="7" height="10" style="color:var(--accent)"><use href="#i-updown"/></svg>13</div></div>

  <div class="league"><svg class="ic" width="11" height="11" style="color:#fff"><use href="#i-star"/></svg><span class="name">Southern Coast Premier league</span><svg class="ic" width="14" height="14" style="color:#fff"><use href="#i-refresh"/></svg></div>
  <div class="grid row"><div class="time"><svg width="13" height="11" style="color:var(--accent)"><use href="#i-chart"/></svg><span>16 : 30<br>Live</span></div><div class="ev"><svg width="10" height="10" style="color:#222a36"><use href="#i-star"/></svg><span>Harbour Mariners<br>Riverside Victory<br>Draw</span></div><div>0-0.5</div><div>0.77<br>-0.95</div><div>6-6.5</div><div class="x12">O -0.85<br>U -0.65</div><div class="more"><svg width="7" height="10" style="color:var(--accent)"><use href="#i-updown"/></svg>13</div></div>
  <div class="grid row"><div class="time"><svg width="13" height="11" style="color:var(--accent)"><use href="#i-chart"/></svg><span>16 : 30<br>Live</span></div><div class="ev"><svg width="10" height="10" style="color:#222a36"><use href="#i-star"/></svg><span>Harbour Mariners<br>Riverside Victory<br>Draw</span></div><div>0-0.5</div><div>0.77<br>-0.95</div><div>6-6.5</div><div class="x12">O -0.85<br>U -0.65</div><div class="more"><svg width="7" height="10" style="color:var(--accent)"><use href="#i-updown"/></svg>13</div></div>
  <div class="grid row"><div class="time"><svg width="13" height="11" style="color:var(--accent)"><use href="#i-chart"/></svg><span>16 : 30<br>Live</span></div><div class="ev"><svg width="10" height="10" style="color:#222a36"><use href="#i-star"/></svg><span>Harbour Mariners<br>Riverside Victory<br>Draw</span></div><div>0-0.5</div><div>0.77<br>-0.95</div><div>6-6.5</div><div class="x12">O -0.85<br>U -0.65</div><div class="more"><svg width="7" height="10" style="color:var(--accent)"><use href="#i-updown"/></svg>13</div></div>

  <div class="league"><svg class="ic" width="11" height="11" style="color:#fff"><use href="#i-star"/></svg><span class="name">Southern Coast Premier league</span><svg class="ic" width="14" height="14" style="color:#fff"><use href="#i-refresh"/></svg></div>
  <div class="grid row"><div class="time"><svg width="13" height="11" style="color:var(--accent)"><use href="#i-chart"/></svg><span>16 : 30<br>Live</span></div><div class="ev"><svg width="10" height="10" style="color:#222a36"><use href="#i-star"/></svg><span>Harbour Mariners<br>Riverside Victory<br>Draw</span></div><div>0-0.5</div><div>0.77<br>-0.95</div><div>6-6.5</div><div class="x12">O -0.85<br>U -0.65</div><div class="more"><svg width="7" height="10" style="color:var(--accent)"><use href="#i-updown"/></svg>13</div></div>

  <div class="league"><svg class="ic" width="11" height="11" style="color:#fff"><use href="#i-star"/></svg><span class="name">Southern Coast Premier league</span><svg class="ic" width="14" height="14" style="color:#fff"><use href="#i-refresh"/></svg></div>
  <div class="grid row"><div class="time"><svg width="13" height="11" style="color:var(--accent)"><use href="#i-chart"/></svg><span>16 : 30<br>Live</span></div><div class="ev"><svg width="10" height="10" style="color:#222a36"><use href="#i-star"/></svg><span>Harbour Mariners<br>Riverside Victory<br>Draw</span></div><div>0-0.5</div><div>0.77<br>-0.95</div><div>6-6.5</div><div class="x12">O -0.85<br>U -0.65</div><div class="more"><svg width="7" height="10" style="color:var(--accent)"><use href="#i-updown"/></svg>13</div></div>
  <div class="grid row"><div class="time"><svg width="13" height="11" style="color:var(--accent)"><use href="#i-chart"/></svg><span>16 : 30<br>Live</span></div><div class="ev"><svg width="10" height="10" style="color:#222a36"><use href="#i-star"/></svg><span>Harbour Mariners<br>Riverside Victory<br>Draw</span></div><div>0-0.5</div><div>0.77<br>-0.95</div><div>6-6.5</div><div class="x12">O -0.85<br>U -0.65</div><div class="more"><svg width="7" height="10" style="color:var(--accent)"><use href="#i-updown"/></svg>13</div></div>
  <div class="grid row"><div class="time"><svg width="13" height="11" style="color:var(--accent)"><use href="#i-chart"/></svg><span>16 : 30<br>Live</span></div><div class="ev"><svg width="10" height="10" style="color:#222a36"><use href="#i-star"/></svg><span>Harbour Mariners<br>Riverside Victory<br>Draw</span></div><div>0-0.5</div><div>0.77<br>-0.95</div><div>6-6.5</div><div class="x12">O -0.85<br>U -0.65</div><div class="more"><svg width="7" height="10" style="color:var(--accent)"><use href="#i-updown"/></svg>13</div></div>
  <div class="grid row"><div class="time"><svg width="13" height="11" style="color:var(--accent)"><use href="#i-chart"/></svg><span>16 : 30<br>Live</span></div><div class="ev"><svg width="10" height="10" style="color:#222a36"><use href="#i-star"/></svg><span>Harbour Mariners<br>Riverside Victory<br>Draw</span></div><div>0-0.5</div><div>0.77<br>-0.95</div><div>6-6.5</div><div class="x12">O -0.85<br>U -0.65</div><div class="more"><svg width="7" height="10" style="color:var(--accent)"><use href="#i-updown"/></svg>13</div></div>
  <div class="grid row"><div class="time"><svg width="13" height="11" style="color:var(--accent)"><use href="#i-chart"/></svg><span>16 : 30<br>Live</span></div><div class="ev"><svg width="10" height="10" style="color:#222a36"><use href="#i-star"/></svg><span>Harbour Mariners<br>Riverside Victory<br>Draw</span></div><div>0-0.5</div><div>0.77<br>-0.95</div><div>6-6.5</div><div class="x12">O -0.85<br>U -0.65</div><div class="more"><svg width="7" height="10" style="color:var(--accent)"><use href="#i-updown"/></svg>13</div></div>
  <div class="grid row"><div class="time"><svg width="13" height="11" style="color:var(--accent)"><use href="#i-chart"/></svg><span>16 : 30<br>Live</span></div><div class="ev"><svg width="10" height="10" style="color:#222a36"><use href="#i-star"/></svg><span>Harbour Mariners<br>Riverside Victory<br>Draw</span></div><div>0-0.5</div><div>0.77<br>-0.95</div><div>6-6.5</div><div class="x12">O -0.85<br>U -0.65</div><div class="more"><svg width="7" height="10" style="color:var(--accent)"><use href="#i-updown"/></svg>13</div></div>
  <div class="grid row"><div class="time"><svg width="13" height="11" style="color:var(--accent)"><use href="#i-chart"/></svg><span>16 : 30<br>Live</span></div><div class="ev"><svg width="10" height="10" style="color:#222a36"><use href="#i-star"/></svg><span>Harbour Mariners<br>Riverside Victory<br>Draw</span></div><div>0-0.5</div><div>0.77<br>-0.95</div><div>6-6.5</div><div class="x12">O -0.85<br>U -0.65</div><div class="more"><svg width="7" height="10" style="color:var(--accent)"><use href="#i-updown"/></svg>13</div></div>
  <div class="grid row"><div class="time"><svg width="13" height="11" style="color:var(--accent)"><use href="#i-chart"/></svg><span>16 : 30<br>Live</span></div><div class="ev"><svg width="10" height="10" style="color:#222a36"><use href="#i-star"/></svg><span>Harbour Mariners<br>Riverside Victory<br>Draw</span></div><div>0-0.5</div><div>0.77<br>-0.95</div><div>6-6.5</div><div class="x12">O -0.85<br>U -0.65</div><div class="more"><svg width="7" height="10" style="color:var(--accent)"><use href="#i-updown"/></svg>13</div></div>
</section>

<div class="abs footer">Betting Rules<span>|</span>Contact Us<span>|</span>Privacy Policy<span>|</span>Responsible Gambling<span>|</span>Terms &amp; Conditions<span>|</span>Tutorials</div>
</body>
</html>
```